Cleaning Company Website Design

I am looking for a website design that has my contact information on each page (Call or Text and my e-mail). It should have the main landing page and than pages for Residential Cleaning (Move In/Move Out, Weekly, and Bi-Weekly Cleaning), Commercial Cleaning (Move In/Move Out, Weekly, and Bi-Weekly Cleaning), New Construction Cleaning (Residential, Commercial, and Industrial), and Apartment Turn cleaning for Property Managers. It should list that we carry insurance as well.

Target Market(s)

Residential and Commercial Customers

Industry/Entity Type

Cleaning

Coding

Coded - Design and coding required

Number of Pages Required

5+ page

Requirements
Must have
• A clean professional looking website

```html
<!DOCTYPE html>
<html lang="en">
<head>
<meta charset="utf-8">
<title>BrightNest Cleaning</title>
<link rel="stylesheet" href="https://fonts.googleapis.com/css2?family=Rubik:wght@500;600;700;800&family=Poppins:wght@400;500;600&display=swap">
<style>
:root{
  --blue:#0d5ba8;
  --blue-dark:#0a4a8f;
  --navy:#0b4c93;
  --teal:#1db4a0;
  --teal-dark:#17a290;
  --grey-bg:#eeeeee;
  --text:#555b63;
  --ink:#1d2530;
  --white:#ffffff;
}
*{box-sizing:border-box;margin:0;padding:0}
html,body{width:1200px;height:4566px;overflow:hidden}
body{font-family:'Poppins',sans-serif;color:var(--text);background:var(--white);position:relative}
.abs{position:absolute}
section,header,footer{position:absolute;left:0;width:1200px}
.eyebrow{font-family:'Rubik',sans-serif;font-weight:600;font-size:19px;color:var(--teal);letter-spacing:.3px;display:flex;align-items:center;gap:12px;white-space:nowrap}
.eyebrow .rule{display:inline-block;width:42px;height:2px;background:var(--teal)}
.eyebrow.center{justify-content:center}
.eyebrow.center .rule{width:68px}
.heading{font-family:'Rubik',sans-serif;font-weight:800;font-size:47px;line-height:1;color:var(--navy);text-transform:uppercase}
.heading.center{text-align:center}
.btn{display:inline-flex;align-items:center;gap:12px;height:40px;padding:0 6px 0 20px;border-radius:22px;background:var(--blue);color:var(--white);font-family:'Rubik',sans-serif;font-weight:600;font-size:14px;text-transform:uppercase;letter-spacing:.3px}
.btn .dot{width:30px;height:30px;border-radius:50%;background:var(--white);display:flex;align-items:center;justify-content:center}
.btn .dot svg{width:16px;height:16px;color:var(--blue)}
.btn.light{background:#dce9f5;color:var(--navy);font-size:12px;height:34px;padding-left:18px}
.btn.light .dot{background:var(--blue);width:26px;height:26px}
.btn.light .dot svg{color:var(--white);width:14px;height:14px}
.btn.white{background:var(--white);color:var(--blue)}
.btn.white .dot{background:var(--blue)}
.btn.white .dot svg{color:var(--white)}
.circle-nav{width:42px;height:42px;border-radius:50%;display:flex;align-items:center;justify-content:center}
.circle-nav svg{width:18px;height:18px}
.photo{background:linear-gradient(135deg,#cfd9e2,#9fb1c2)}

/* top bar */
.topbar{top:0;height:35px;background:var(--blue);color:var(--white);font-size:12px}
.topbar .item{position:absolute;top:0;height:35px;display:flex;align-items:center;gap:8px}
.topbar svg{width:14px;height:14px;color:var(--white)}
/* nav */
.nav{top:35px;height:54px;background:var(--white);z-index:3}
.nav a{position:absolute;top:18px;font-size:13px;font-weight:500;color:var(--blue);text-decoration:none}
.logo-tab{position:absolute;left:526px;top:-8px;width:148px;height:130px;border-radius:0 0 74px 74px;background:var(--white);border-bottom:4px solid var(--blue);display:flex;align-items:center;justify-content:center;flex-direction:column;padding-top:34px}
.brand{font-family:'Rubik',sans-serif;font-weight:600;color:var(--teal);letter-spacing:1px;line-height:1.1;text-align:center}
.nav .contact-btn{position:absolute;left:907px;top:8px;height:38px;font-size:13px;text-transform:none;padding-left:18px}
.nav .search{position:absolute;left:1026px;top:16px;width:24px;height:24px;color:var(--blue)}

/* hero */
.hero{top:89px;height:584px;background:linear-gradient(90deg,#dedede 0%,#e8e8e8 40%,#d9d9d9 100%);overflow:hidden}
.hero .photo-hero{position:absolute;left:520px;top:0;width:680px;height:584px;background:linear-gradient(120deg,#d6d6d6 0%,#c7ccd2 45%,#8fa9c6 70%,#e2e2e2 100%)}
.hero .photo-left{position:absolute;left:0;top:0;width:200px;height:380px;background:linear-gradient(160deg,#cfcfcf,#e4e4e4)}
.hero-title{position:absolute;left:149px;font-family:'Rubik',sans-serif;font-weight:800;font-size:52px;line-height:1;color:var(--white);text-transform:uppercase;white-space:nowrap}
.hero-title .teal{color:var(--teal)}
.hero .book{position:absolute;left:301px;top:306px;height:44px}
.hero .arrows{position:absolute;left:150px;top:362px;display:flex;flex-direction:column;gap:8px}

/* about */
.about{top:673px;height:577px;background:var(--white)}
.about .ring{position:absolute;left:146px;top:50px;width:452px;height:436px;border-radius:50%;background:var(--teal)}
.about .photo-about{position:absolute;left:149px;top:45px;width:438px;height:438px;border-radius:50%;background:linear-gradient(135deg,#e7ecef,#bcc7cf 60%,#8aa0b4)}
.about p{font-size:11.4px;line-height:20px;color:var(--text)}

/* services */
.services{top:1250px;height:673px;background:var(--blue)}
.services .eyebrow{color:var(--white)}
.services .eyebrow .rule{background:var(--white)}
.services .heading{color:var(--white)}
.svc{position:absolute;top:200px;width:289px;height:384px;background:var(--white);border-radius:4px;overflow:hidden;text-align:center}
.svc .photo{height:191px}
.svc .icon{position:absolute;left:109px;top:154px;width:72px;height:72px;border-radius:50%;background:var(--blue);border:5px solid var(--teal);display:flex;align-items:center;justify-content:center}
.svc .icon svg{width:30px;height:30px;color:var(--white)}
.svc h3{margin-top:50px;font-family:'Rubik',sans-serif;font-weight:600;font-size:17px;color:var(--navy)}
.svc p{margin:10px auto 0;width:236px;height:36px;font-size:11px;line-height:18px}
.svc .btn{margin-top:18px}

/* why us */
.why{top:1923px;height:588px;background:var(--white)}
.why .ring{position:absolute;left:593px;top:70px;width:450px;height:430px;border-radius:50%;background:var(--blue)}
.why .photo-why{position:absolute;left:601px;top:63px;width:448px;height:448px;border-radius:50%;background:linear-gradient(150deg,#f2f2f2,#c8cdd1 55%,#3a9a6a 75%,#e9e9e9)}
.feat{position:absolute;left:149px;width:400px;display:flex;gap:20px}
.feat .ic{flex:none;width:52px;height:52px;border-radius:50%;background:var(--white);box-shadow:0 3px 12px rgba(0,0,0,.12);display:flex;align-items:center;justify-content:center}
.feat .ic svg{width:26px;height:26px;color:var(--blue)}
.feat p{font-size:11px;line-height:18px;color:var(--text)}
.feat p b{color:var(--ink);font-weight:600}

/* testimonials */
.testi{top:2511px;height:573px;background:var(--grey-bg)}
.quote{position:absolute;top:242px;width:442px;height:246px;background:var(--white);border-radius:6px;box-shadow:0 4px 14px rgba(0,0,0,.06)}
.quote .avatar{position:absolute;left:40px;top:38px;width:78px;height:78px;border-radius:50%;background:linear-gradient(135deg,#c9b7a6,#6c5a4d)}
.quote .name{position:absolute;left:144px;top:52px;font-family:'Rubik',sans-serif;font-weight:500;font-size:16px;color:var(--navy)}
.quote .role{position:absolute;left:144px;top:76px;font-size:11px;color:var(--text)}
.quote .stars{position:absolute;left:144px;top:96px;display:flex;gap:2px}
.quote .stars svg{width:15px;height:15px;color:#f5a623}
.quote p{position:absolute;left:42px;top:140px;width:365px;font-size:10.4px;line-height:20px}

/* contact */
.contact{top:3084px;height:514px;background:var(--teal)}
.contact .photo-contact{position:absolute;left:0;top:0;width:570px;height:514px;background:linear-gradient(135deg,#dfe5ea,#a9b6c1 50%,#e9eef1);clip-path:path('M0 0 H500 C600 130 600 380 470 514 H0 Z')}
.contact .edge{position:absolute;left:0;top:0}
.contact .eyebrow{color:var(--white)}
.contact .eyebrow .rule{background:var(--white);width:64px}
.contact .heading{color:var(--white)}
.field{position:absolute;height:45px;border:1px solid rgba(255,255,255,.5);background:rgba(255,255,255,.14);border-radius:3px;color:var(--white);font-size:11px;padding:13px 18px}

/* blog */
.blog{top:3598px;height:649px;background:var(--white)}
.post{position:absolute;top:213px;width:286px;height:360px;background:var(--white);box-shadow:0 3px 14px rgba(0,0,0,.09);border-bottom:4px solid var(--teal)}
.post .photo{position:absolute;left:12px;top:12px;width:262px;height:175px}
.post .meta{position:absolute;left:12px;top:200px;font-size:9px;color:var(--text);display:flex;gap:28px}
.post h4{position:absolute;left:12px;top:220px;width:250px;font-family:'Poppins',sans-serif;font-weight:600;font-size:13.5px;line-height:19px;color:var(--ink)}
.post p{position:absolute;left:12px;top:268px;width:260px;font-size:9.5px;line-height:17px}
.post .more{position:absolute;left:12px;top:313px;font-size:13px;font-weight:600;color:var(--blue);display:flex;align-items:center;gap:6px}
.post .more svg{width:20px;height:14px;color:var(--blue)}

/* footer */
.footer{top:4247px;height:319px;background:var(--blue);color:var(--white)}
.footer h5{position:absolute;top:78px;font-family:'Rubik',sans-serif;font-weight:700;font-size:16px;text-transform:uppercase;color:var(--white)}
.footer ul{position:absolute;top:110px;list-style:none;font-size:11.5px;line-height:22.5px}
.footer .ci{position:absolute;left:557px;display:flex;gap:14px;font-size:11.5px;line-height:22px}
.footer .ci svg{flex:none;width:16px;height:16px;margin-top:3px;color:var(--white)}
.footer .news{position:absolute;left:771px;top:114px;width:281px;height:44px;border:1px solid rgba(255,255,255,.7);border-radius:22px;display:flex;align-items:center;justify-content:space-between;padding:0 4px 0 20px;font-size:11px}
.footer .news .btn{height:36px;font-size:12px}
.footer .divider{position:absolute;left:149px;top:274px;width:903px;height:1px;background:rgba(255,255,255,.3)}
.footer .social{position:absolute;left:149px;top:287px;display:flex;gap:7px}
.footer .social span{width:22px;height:22px;border-radius:50%;background:var(--white)}
.footer .copy{position:absolute;right:148px;top:290px;font-size:11px}
</style>
</head>
<body>
<svg width="0" height="0" style="position:absolute">
  <defs>
    <symbol id="i-arrow" viewBox="0 0 16 16"><path d="M3 8h10M9 4l4 4-4 4" fill="none" stroke="currentColor" stroke-width="2" stroke-linecap="round" stroke-linejoin="round"/></symbol>
    <symbol id="i-left" viewBox="0 0 16 16"><path d="M10 3 5 8l5 5" fill="none" stroke="currentColor" stroke-width="2" stroke-linecap="round" stroke-linejoin="round"/></symbol>
    <symbol id="i-right" viewBox="0 0 16 16"><path d="M6 3l5 5-5 5" fill="none" stroke="currentColor" stroke-width="2" stroke-linecap="round" stroke-linejoin="round"/></symbol>
    <symbol id="i-pin" viewBox="0 0 16 16"><path d="M8 1a5 5 0 0 0-5 5c0 4 5 9 5 9s5-5 5-9a5 5 0 0 0-5-5zm0 7a2 2 0 1 1 0-4 2 2 0 0 1 0 4z" fill="currentColor"/></symbol>
    <symbol id="i-mail" viewBox="0 0 16 16"><rect x="1" y="3" width="14" height="10" rx="1" fill="none" stroke="currentColor" stroke-width="1.6"/><path d="M1.5 3.5 8 9l6.5-5.5" fill="none" stroke="currentColor" stroke-width="1.6"/></symbol>
    <symbol id="i-phone" viewBox="0 0 16 16"><path d="M4 1.5 6.3 4 5 6c.8 2 2.5 3.7 5 5l2-1.3 2.5 2.3-1.6 2.2C7.5 14 2 8.5 1.8 3.1z" fill="currentColor"/></symbol>
    <symbol id="i-star" viewBox="0 0 16 16"><path d="m8 1 2.1 4.6 5 .5-3.8 3.3 1.1 4.9L8 11.8l-4.4 2.5 1.1-4.9L.9 6.1l5-.5z" fill="currentColor"/></symbol>
    <symbol id="i-home" viewBox="0 0 24 24"><path d="M3 11 12 3l9 8v10h-6v-6H9v6H3z" fill="currentColor"/></symbol>
    <symbol id="i-building" viewBox="0 0 24 24"><path d="M4 21V5l8-3v19zm10 0V9h6v12z" fill="currentColor"/><path d="M6 7h4M6 11h4M6 15h4M16 12h2M16 16h2" stroke="#0d5ba8" stroke-width="1.5"/></symbol>
    <symbol id="i-spray" viewBox="0 0 24 24"><path d="M9 2h5v3h3v2h-3v2h2l1 3v10H7V12l1-3h1z" fill="currentColor"/></symbol>
    <symbol id="i-tick" viewBox="0 0 24 24"><circle cx="12" cy="12" r="10" fill="none" stroke="currentColor" stroke-width="2"/><path d="m7 12 3.5 3.5L17 9" fill="none" stroke="currentColor" stroke-width="2.2" stroke-linecap="round"/></symbol>
    <symbol id="i-bell" viewBox="0 0 24 24"><path d="M12 3a6 6 0 0 0-6 6v5l-2 3h16l-2-3V9a6 6 0 0 0-6-6zM10 19a2 2 0 0 0 4 0" fill="currentColor"/></symbol>
    <symbol id="i-team" viewBox="0 0 24 24"><circle cx="12" cy="6" r="3" fill="currentColor"/><circle cx="5" cy="13" r="2.5" fill="currentColor"/><circle cx="19" cy="13" r="2.5" fill="currentColor"/><path d="M7 21c0-3 2-6 5-6s5 3 5 6zM1 21c0-2.5 1.5-4.5 4-4.5M23 21c0-2.5-1.5-4.5-4-4.5" fill="currentColor"/></symbol>
    <symbol id="i-search" viewBox="0 0 24 24"><circle cx="10" cy="10" r="7" fill="none" stroke="currentColor" stroke-width="2.4"/><path d="m15 15 6 6" stroke="currentColor" stroke-width="2.4" stroke-linecap="round"/></symbol>
  </defs>
</svg>

<!-- top bar -->
<header class="topbar">
  <div class="item" style="left:149px"><svg><use href="#i-pin"/></svg>412 Maple Grove Avenue, Springfield, USA</div>
  <div class="item" style="left:543px"><svg><use href="#i-mail"/></svg>hello@brightnestclean.com</div>
  <div class="item" style="left:935px"><svg><use href="#i-phone"/></svg>Call or Text (555) 014-2207</div>
</header>

<!-- navigation -->
<header class="nav">
  <a style="left:149px">Home</a>
  <a style="left:236px">About Us</a>
  <a style="left:342px">Services ▾</a>
  <a style="left:445px">Pricing</a>
  <div class="logo-tab"><div class="brand" style="font-size:17px">BRIGHTNEST</div><div class="brand" style="font-size:9px;letter-spacing:2px">CLEANING</div></div>
  <a style="left:707px">Testimonials</a>
  <a style="left:836px">Blog</a>
  <div class="btn contact-btn">Contact <span class="dot"><svg><use href="#i-arrow"/></svg></span></div>
  <svg class="search"><use href="#i-search"/></svg>
</header>

<!-- hero -->
<section class="hero">
  <div class="photo-left" role="img" aria-label="Faded cleaning tools in the background"></div>
  <div class="photo-hero" role="img" aria-label="Cleaner in mask and blue gloves spraying a surface"></div>
  <div class="eyebrow abs" style="left:239px;top:152px;color:var(--white)"><span class="rule" style="background:var(--teal);width:56px"></span><span><span style="color:var(--navy)">BRIGHTNEST</span> CLEANING</span></div>
  <div class="hero-title" style="top:186px">Best <span class="teal">Cleaning</span></div>
  <div class="hero-title" style="left:232px;top:240px">Services</div>
  <div class="btn book">Book now <span class="dot"><svg><use href="#i-arrow"/></svg></span></div>
  <div class="arrows">
    <div class="circle-nav" style="background:var(--teal);color:var(--white)"><svg><use href="#i-right"/></svg></div>
    <div class="circle-nav" style="background:#cfd7dc;color:var(--teal)"><svg><use href="#i-left"/></svg></div>
  </div>
  <svg class="abs" style="left:0;top:440px" width="1200" height="144" viewBox="0 0 1200 144">
    <path d="M0 84 C60 70 120 90 180 78 C240 60 300 100 380 112 C600 140 900 140 1200 60 V144 H0Z" fill="#fff"/>
    <path d="M380 112 C650 150 950 135 1200 62 V88 C950 160 650 175 380 112Z" fill="#1db4a0"/>
  </svg>
</section>

<!-- about -->
<section class="about">
  <div class="ring"></div>
  <div class="photo-about" role="img" aria-label="Smiling cleaner in mask and yellow gloves giving a thumbs up"></div>
  <div class="eyebrow abs" style="left:650px;top:90px">BRIGHTNEST CLEANING <span class="rule"></span></div>
  <div class="heading abs" style="left:650px;top:116px">About Us</div>
  <p class="abs" style="left:650px;top:168px;width:390px">We are a locally owned cleaning company serving homes, offices and rental properties. We carry full liability insurance, so every visit is covered.</p>
  <p class="abs" style="left:650px;top:248px;width:395px">We offer Residential and Commercial cleaning with Move In/Move Out, Weekly and Bi-Weekly plans, New Construction cleaning for residential, commercial and industrial sites, and Apartment Turn cleaning for property managers who need units ready for the next tenant. Call or text us any time for a free quote and friendly help.</p>
  <div class="btn abs" style="left:650px;top:390px">Read more <span class="dot"><svg><use href="#i-arrow"/></svg></span></div>
</section>

<!-- services -->
<section class="services">
  <div class="eyebrow center abs" style="left:0;width:1200px;top:74px"><span class="rule"></span>BRIGHTNEST CLEANING<span class="rule"></span></div>
  <div class="heading center abs" style="left:0;width:1200px;top:108px">Best Services</div>
  <div class="abs" style="left:956px;top:121px;display:flex;gap:8px">
    <div class="circle-nav" style="border:1px solid rgba(255,255,255,.6);color:var(--white)"><svg><use href="#i-left"/></svg></div>
    <div class="circle-nav" style="background:rgba(255,255,255,.25);color:var(--white)"><svg><use href="#i-right"/></svg></div>
  </div>
  <div class="svc" style="left:149px">
    <div class="photo" role="img" aria-label="Cleaners tidying a bright home interior" style="background:linear-gradient(135deg,#e6dcc7,#b7a78c 60%,#7d8a99)"></div>
    <div class="icon"><svg><use href="#i-home"/></svg></div>
    <h3>Residential Cleaning</h3>
    <p>Move In/Move Out, Weekly and Bi-Weekly cleaning for your home.</p>
    <div class="btn light">Read more <span class="dot"><svg><use href="#i-arrow"/></svg></span></div>
  </div>
  <div class="svc" style="left:455px">
    <div class="photo" role="img" aria-label="Cleaner mopping an office floor" style="background:linear-gradient(135deg,#cfd3d6,#8c8f93 55%,#5c4e44)"></div>
    <div class="icon"><svg><use href="#i-building"/></svg></div>
    <h3>Commercial Cleaning</h3>
    <p>Move In/Move Out, Weekly and Bi-Weekly cleaning for businesses.</p>
    <div class="btn light">Read more <span class="dot"><svg><use href="#i-arrow"/></svg></span></div>
  </div>
  <div class="svc" style="left:762px">
    <div class="photo" role="img" aria-label="Gloved hand wiping a surface with a cloth" style="background:linear-gradient(135deg,#f0f2f4,#c3ccd6 55%,#7ea0c4)"></div>
    <div class="icon"><svg><use href="#i-spray"/></svg></div>
    <h3>Construction Cleaning</h3>
    <p>New construction cleaning for residential, commercial and industrial.</p>
    <div class="btn light">Read more <span class="dot"><svg><use href="#i-arrow"/></svg></span></div>
  </div>
</section>

<!-- why us -->
<section class="why">
  <div class="ring"></div>
  <div class="photo-why" role="img" aria-label="Cleaner in green apron mopping a living room floor"></div>
  <div class="eyebrow abs" style="left:151px;top:137px">BRIGHTNEST CLEANING <span class="rule" style="width:28px"></span></div>
  <div class="heading abs" style="left:151px;top:168px;color:var(--teal)">What Us</div>
  <div class="feat" style="top:236px"><div class="ic"><svg><use href="#i-tick"/></svg></div><p><b>Thanks to professional-grade equipment, customized solutions</b> and a team that takes a lot of pride in a job well done, we're able to produce results that impress.</p></div>
  <div class="feat" style="top:312px"><div class="ic"><svg><use href="#i-bell"/></svg></div><p><b>Apartment Turn cleaning for Property Managers,</b> with fast turnaround so every unit is ready for the next tenant.</p></div>
  <div class="feat" style="top:376px"><div class="ic"><svg><use href="#i-team"/></svg></div><p><b>We are fully licensed and insured,</b> so your home, office or property is protected on every single visit we make.</p></div>
</section>

<!-- testimonials -->
<section class="testi">
  <div class="eyebrow center abs" style="left:0;width:1200px;top:76px"><span class="rule"></span>BRIGHTNEST CLEANING<span class="rule"></span></div>
  <div class="heading center abs" style="left:0;width:1200px;top:108px">What our client</div>
  <div class="heading center abs" style="left:0;width:1200px;top:152px;color:var(--teal)">Says</div>
  <div class="abs" style="left:956px;top:169px;display:flex;gap:8px">
    <div class="circle-nav" style="background:var(--white);color:var(--ink)"><svg><use href="#i-left"/></svg></div>
    <div class="circle-nav" style="background:var(--white);color:var(--ink)"><svg><use href="#i-right"/></svg></div>
  </div>
  <div class="quote" style="left:149px">
    <div class="avatar" role="img" aria-label="Client portrait"></div>
    <div class="name">Laura Bennett</div><div class="role">Marketing Manager</div>
    <div class="stars"><svg><use href="#i-star"/></svg><svg><use href="#i-star"/></svg><svg><use href="#i-star"/></svg><svg><use href="#i-star"/></svg><svg><use href="#i-star"/></svg></div>
    <p>Lorem ipsum dolor sit amet, consectetur adipiscing elit. Proin in amet pretium leo. Etiam congue magna nisi. Curabitur sit amet laoreet enim. Morbi sed erat efficitur neque iaculis tempor sit amet vel erat laoreet enim.Morbi sed erat efficitur neque.</p>
  </div>
  <div class="quote" style="left:610px">
    <div class="avatar" role="img" aria-label="Client portrait" style="background:linear-gradient(135deg,#c4c9cf,#4e5967)"></div>
    <div class="name">Daniel Hayes</div><div class="role">Marketing Manager</div>
    <div class="stars"><svg><use href="#i-star"/></svg><svg><use href="#i-star"/></svg><svg><use href="#i-star"/></svg><svg><use href="#i-star"/></svg><svg><use href="#i-star"/></svg></div>
    <p>Lorem ipsum dolor sit amet, consectetur adipiscing elit. Proin in amet pretium leo. Etiam congue magna nisi. Curabitur sit amet laoreet enim. Morbi sed erat efficitur neque iaculis tempor sit amet vel erat laoreet enim.Morbi sed erat efficitur neque.</p>
  </div>
</section>

<!-- contact -->
<section class="contact">
  <svg class="edge" width="600" height="514" viewBox="0 0 600 514"><path d="M500 0 C614 130 614 380 470 514" fill="none" stroke="#fff" stroke-width="10"/></svg>
  <div class="photo-contact" role="img" aria-label="Gloved hand spraying cleaner on a desk"></div>
  <div class="eyebrow abs" style="left:642px;top:74px">BRIGHTNEST CLEANING <span class="rule"></span></div>
  <div class="heading abs" style="left:642px;top:106px">Contact Now</div>
  <div class="field" style="left:642px;top:177px;width:193px">Full Name</div>
  <div class="field" style="left:846px;top:177px;width:194px">Your Email</div>
  <div class="field" style="left:642px;top:234px;width:193px">Phone Number</div>
  <div class="field" style="left:846px;top:234px;width:194px">Select Services</div>
  <div class="field" style="left:642px;top:291px;width:398px;height:92px">Message</div>
  <div class="btn white abs" style="left:642px;top:396px">Submit <span class="dot"><svg><use href="#i-arrow"/></svg></span></div>
</section>

<!-- blog -->
<section class="blog">
  <div class="eyebrow center abs" style="left:0;width:1200px;top:96px"><span class="rule" style="width:55px"></span>BRIGHTNEST CLEANING<span class="rule" style="width:55px"></span></div>
  <div class="heading center abs" style="left:0;width:1200px;top:128px;color:var(--teal)">Latest Blog</div>
  <div class="post" style="left:151px">
    <div class="photo" role="img" aria-label="Person mopping a wooden floor" style="background:linear-gradient(135deg,#e6e6e6,#a9a29a 55%,#4f4a45)"></div>
    <div class="meta"><span>What's New</span><span>December 7, 2022</span></div>
    <h4>Use soap and water to clean your kitchen shelves too</h4>
    <p>Lorem ipsum dolor sit amet, consectetur adipiscing elit, sed do eiusmod tempor .......</p>
    <div class="more">Read More <svg viewBox="0 0 20 14"><path d="M1 7h17M13 2l5 5-5 5" fill="none" stroke="currentColor" stroke-width="1.6"/></svg></div>
  </div>
  <div class="post" style="left:459px">
    <div class="photo" role="img" aria-label="Empty restaurant dining room" style="background:linear-gradient(135deg,#4c4038,#8c7664 50%,#cfc6b8)"></div>
    <div class="meta"><span>What's New</span><span>December 7, 2022</span></div>
    <h4>A quick solutions for daily house cleaning problem</h4>
    <p>Lorem ipsum dolor sit amet, consectetur adipiscing elit, sed do eiusmod tempor .......</p>
    <div class="more">Read More <svg viewBox="0 0 20 14"><path d="M1 7h17M13 2l5 5-5 5" fill="none" stroke="currentColor" stroke-width="1.6"/></svg></div>
  </div>
  <div class="post" style="left:767px">
    <div class="photo" role="img" aria-label="Gloved hand holding a spray bottle" style="background:linear-gradient(135deg,#eef0f2,#9cb4d6 55%,#4f77b3)"></div>
    <div class="meta"><span>What's New</span><span>December 7, 2022</span></div>
    <h4>A quick solutions for daily house cleaning problem</h4>
    <p>Lorem ipsum dolor sit amet, consectetur adipiscing elit, sed do eiusmod tempor .......</p>
    <div class="more">Read More <svg viewBox="0 0 20 14"><path d="M1 7h17M13 2l5 5-5 5" fill="none" stroke="currentColor" stroke-width="1.6"/></svg></div>
  </div>
</section>

<!-- footer -->
<footer class="footer">
  <div class="abs" style="left:149px;top:98px;width:178px;text-align:center">
    <div class="brand" style="color:var(--white);font-size:28px;font-weight:500">BRIGHTNEST</div>
    <div class="brand" style="color:var(--white);font-size:14px;font-weight:500;letter-spacing:4px;margin-top:4px">CLEANING</div>
  </div>
  <h5 style="left:388px">Quick Link</h5>
  <ul style="left:388px"><li>Home</li><li>About Us</li><li>Services</li><li>Why Choose Us</li><li>Blog</li><li>Testimonials</li></ul>
  <h5 style="left:557px">Contact Us</h5>
  <div class="ci" style="top:110px"><svg><use href="#i-phone"/></svg><span>+(1)-555-010-4477</span></div>
  <div class="ci" style="top:134px"><svg><use href="#i-pin"/></svg><span>720 Lakeside Blvd #204,<br>Riverton TX 75000</span></div>
  <div class="ci" style="top:190px"><svg><use href="#i-mail"/></svg><span>www.brightnestclean.com</span></div>
  <h5 style="left:771px">Subscribe to our newsletter</h5>
  <div class="news"><span>Enter your email</span><span class="btn white">Subscribe <span class="dot"><svg><use href="#i-arrow"/></svg></span></span></div>
  <div class="divider"></div>
  <div class="social"><span></span><span></span><span></span><span></span><span></span></div>
  <div class="copy">Copyright © 2023 BrightNest Cleaning All Rights Reserved.</div>
</footer>
</body>
</html>
```